Brochure Design Project for Home Watch company

We are a new start up company in fast growing home watch industry. We provide services in Hawaii so the design needs to be reflect that. Our web site can give you overview of what we do - www.breezekeepcare.com. We will service clients that own second homes in Hawaii. These properties are not necessarily income producing properties for our clients. I'm looking for 2 or 4 page brochure which will be used to market our services to potential new clients. It needs to be high quality, modern with slight Hawaiian feel (we are based on Oahu). I'm not looking for a trifold type of brochure.

We are open to various colors based on what the designer might suggest but as you can see on our home page - the main picture of the home on our site has lots of red and white which we like as well as the "head" or dot above the "i" in our logo is red. I was not able to upload the file of the main house (purchased on snapmeadow) on here therefore I'll have to provide the original photo to the selected designer at the later time. For now I just uploaded the not purchased copy.

If you have other questions please do let me know. And lastly, I will be looking to create a business card and post card as well.

```html
<!DOCTYPE html>
<html lang="en">
<head>
<meta charset="utf-8">
<title>Breeze Keep Care – Brochure Spread</title>
<link rel="stylesheet" href="https://fonts.googleapis.com/css2?family=Montserrat:wght@400;600;700&family=Noto+Serif:ital,wght@0,400;1,400&display=swap">
<style>
  :root{
    --stage:#2b2b2d;
    --paper:#f4f4f5;
    --paper-shade:#e2e2e4;
    --red:#c8323c;
    --charcoal:#4a4a4c;
    --ink:#1e1e20;
    --text:#2c2c2e;
    --white:#ffffff;
    --sky:#6f9ccc;
    --sea:#2f5f8c;
  }
  *{box-sizing:border-box;margin:0;padding:0}
  html,body{width:1200px;height:789px;overflow:hidden;background:var(--stage)}
  .spread{position:absolute;left:80px;top:26px;width:1040px;height:736px}
  .page{position:absolute;top:0;width:520px;height:736px;overflow:hidden}
  .page--back{left:0;background:linear-gradient(180deg,var(--paper) 0%,var(--paper-shade) 100%)}
  .page--front{left:520px;background:var(--paper)}
  .spine{position:absolute;left:519px;top:0;width:2px;height:736px;background:rgba(0,0,0,.08)}

  /* back page */
  .consult-band{position:absolute;left:0;top:96px;width:470px;height:74px;background:var(--red);
    color:var(--white);font:400 16px/1.35 "Montserrat",sans-serif;text-transform:uppercase;
    padding:14px 0 0 36px;letter-spacing:.5px}
  .consult-band strong{font-weight:700}
  .consult-tab{position:absolute;left:470px;top:86px;width:22px;height:74px;background:var(--charcoal)}
  .contact-list{position:absolute;left:20px;top:232px;width:240px;text-align:center;
    font:400 14px/1.3 "Montserrat",sans-serif;color:var(--text);list-style:none}
  .contact-list li{margin-bottom:16px}
  .contact-list svg{display:block;margin:0 auto 6px;width:16px;height:16px}
  .contact-phone{font-weight:700;font-size:19px}
  .contact-hours{font-size:15px}
  .photo-frame{position:absolute;left:250px;top:190px;width:290px;height:360px;background:var(--ink);padding:12px 0 12px 12px}
  .device-art{position:absolute;left:60px;top:610px;width:200px;height:96px;border-radius:6px;
    background:linear-gradient(135deg,#3a3a3c,#8aa58a 55%,#dfe3e6)}
  .mini-brand{position:absolute;left:320px;top:588px;display:flex;align-items:center;gap:6px}
  .mini-brand .brand-name{font:700 13px/1 "Montserrat",sans-serif;color:var(--ink)}
  .mini-tagline{position:absolute;left:320px;top:606px;font:italic 400 8px/1 "Noto Serif",serif;color:var(--text)}
  .member-badge{position:absolute;left:330px;top:636px;width:140px;height:48px;background:var(--white);
    border:2px solid #2a4f9a;border-radius:3px}

  /* front page */
  .brand{position:absolute;left:60px;top:52px;display:flex;align-items:center;gap:10px}
  .brand-dot{width:14px;height:14px;border-radius:50%;background:var(--red)}
  .brand .brand-name{font:700 24px/1 "Montserrat",sans-serif;color:var(--ink)}
  .brand-tagline{position:absolute;left:84px;top:88px;font:italic 400 13px/1 "Noto Serif",serif;color:var(--text)}
  .top-rule{position:absolute;left:0;top:146px;width:520px;height:5px;background:var(--red)}
  .corner-block{position:absolute;left:300px;top:118px;width:220px;height:34px;background:var(--charcoal)}
  .hero-photo{position:absolute;left:0;top:151px;width:520px;height:349px}
  .photo{width:100%;height:100%;
    background:linear-gradient(180deg,var(--sky) 0%,#cfe0ef 38%,#f1f1ef 52%,var(--sea) 78%,#234866 100%)}
  .bottom-rule{position:absolute;left:0;top:500px;width:520px;height:5px;background:var(--red)}
  .tagline-box{position:absolute;left:190px;top:505px;width:330px;height:104px;background:var(--charcoal);
    color:var(--white);font:italic 400 21px/1.3 "Noto Serif",serif;padding:22px 0 0 24px}
  .front-web{position:absolute;left:228px;top:648px;display:flex;align-items:center;gap:10px;
    font:400 14px/1 "Montserrat",sans-serif;color:var(--text)}
  .front-web svg{width:14px;height:14px}
</style>
</head>
<body>
<main class="spread">
  <section class="page page--back">
    <div class="consult-band">Contact us for <strong>free consultation.</strong><br>You have questions? We have answers!</div>
    <div class="consult-tab"></div>

    <ul class="contact-list">
      <li>
        <svg viewBox="0 0 16 16"><path d="M8 1a5 5 0 0 0-5 5c0 4 5 9 5 9s5-5 5-9a5 5 0 0 0-5-5zm0 7a2 2 0 1 1 0-4 2 2 0 0 1 0 4z" fill="var(--red)"/></svg>
        Breeze Keep Care LLC
      </li>
      <li class="contact-phone">
        <svg viewBox="0 0 16 16"><path d="M4 2l2 3-1.5 1.5a8 8 0 0 0 5 5L11 10l3 2-1 2.5C7 15 1 9 1.5 3z" fill="var(--red)"/></svg>
        808-555-0142
      </li>
      <li>
        <svg viewBox="0 0 16 16"><rect x="1" y="3" width="14" height="10" fill="var(--red)"/><path d="M1 3l7 6 7-6" stroke="#fff" fill="none" stroke-width="1.3"/></svg>
        hello@breezekeepcare.com
      </li>
      <li class="contact-hours">
        <svg viewBox="0 0 16 16"><rect x="1" y="3" width="14" height="12" rx="1" fill="none" stroke="var(--red)" stroke-width="1.6"/><rect x="1" y="3" width="14" height="4" fill="var(--red)"/><rect x="4" y="1" width="2" height="3" fill="var(--red)"/><rect x="10" y="1" width="2" height="3" fill="var(--red)"/></svg>
        Monday-Friday,<br>8am-5pm (PST).
      </li>
      <li>
        <svg viewBox="0 0 16 16"><circle cx="8" cy="8" r="6.5" fill="none" stroke="var(--red)" stroke-width="1.5"/><path d="M1.5 8h13M8 1.5c-3 3-3 10 0 13M8 1.5c3 3 3 10 0 13" stroke="var(--red)" fill="none" stroke-width="1.2"/></svg>
        www.breezekeepcare.com
      </li>
    </ul>

    <div class="device-art" role="img" aria-label="Laptop and tablet showing a house photo and an inspection checklist"></div>

    <div class="photo-frame">
      <div class="photo" role="img" aria-label="Tropical villa with pavilion roof and infinity pool overlooking the ocean"></div>
    </div>

    <div class="mini-brand"><span class="brand-dot" style="width:8px;height:8px;border-radius:50%;background:var(--red)"></span><span class="brand-name">Breeze Keep Care</span></div>
    <p class="mini-tagline">Your Home Watch Company</p>
    <div class="member-badge"></div>
  </section>

  <section class="page page--front">
    <div class="brand"><span class="brand-dot"></span><span class="brand-name">Breeze Keep Care</span></div>
    <p class="brand-tagline">Your Home Watch Company</p>

    <div class="corner-block"></div>
    <div class="top-rule"></div>
    <div class="hero-photo">
      <div class="photo" role="img" aria-label="Tropical villa with pavilion roof and infinity pool overlooking the ocean"></div>
    </div>
    <div class="bottom-rule"></div>

    <h1 class="tagline-box">Providing Premiere Home<br>Watch and Concierge Services</h1>

    <p class="front-web">
      <svg viewBox="0 0 16 16"><circle cx="8" cy="8" r="6.5" fill="none" stroke="var(--red)" stroke-width="1.5"/><path d="M1.5 8h13M8 1.5c-3 3-3 10 0 13M8 1.5c3 3 3 10 0 13" stroke="var(--red)" fill="none" stroke-width="1.2"/></svg>
      www.breezekeepcare.com
    </p>
  </section>
  <div class="spine"></div>
</main>
</body>
</html>
```